Travel Group 'Lydgate Group' needs a new business card design

Lydgate Group is a diverse business specialising in bespoke, tailor made holidays to suit all budgets and we are specialists in planning exciting day/short trips to suit all markets. Our target market is very varied going from the corporate client and as well as people in the community who simply want to experience something special.
We are looking for a card design that will encourage people to look at our websites and social media platforms and to see for themselves the different facets to our business. It is essential that the card has social media icons for Facebook, Twitter and Instagram. We are looking for a card with a blank background with no pictures and for the front side to have the attached Lydgate logo. The card should have similar colour scheme to the attached Lydgate logo.
The card must have the following information on one side:
Maud Penrose
Business Development Manager
maudpenrose@lydgatevoyages.example
Lydgate Group, 87 Quarry Lane
Kilwinning, Ayrshire, Scotland KA19 4TN
+44 (0)1294 730182
And then the card must have the following on the second side:
(Lydgate logo)
(social media icons)
www.lydgatevoyages.example
www.lydgateoutings.example
Target Market(s)
Our target market is very varied going from the corporate client and as well as people in the community who simply want to experience something special.
Industry/Entity Type
Business
Contact Information for Business Card
Maud Penrose
+44 (0)1294 730182
(Lydgate logo)
(social media icons)
www.lydgatevoyages.example
www.lydgateoutings.example
Requirements
Must have
- It is essential that the card has social media icons for Facebook, Twitter & Instagram.
Should not have
- Should not have any images other than Lydgate logo.

```html
<!DOCTYPE html>
<html lang="en">
<head>
<meta charset="utf-8">
<title>Lydgate Group – Business Card</title>
<link rel="stylesheet" href="https://fonts.googleapis.com/css2?family=Arimo:wght@400;700&display=swap">
<style>
  :root {
    --backdrop: #1d1d1f;
    --card-white: #f4f4f4;
    --navy: #2b2470;
    --plum: #7a1f86;
    --magenta: #b3128f;
    --ink: #4a4a4a;
    --rule: #c9c9c9;
    --white: #ffffff;
  }
  * { box-sizing: border-box; margin: 0; padding: 0; }
  html, body { width: 1200px; height: 974px; overflow: hidden; }
  body {
    background: var(--backdrop);
    font-family: "Arimo", Arial, sans-serif;
    display: flex;
    align-items: center;
    justify-content: center;
    gap: 40px;
  }
  .card {
    width: 540px;
    height: 338px;
    border-radius: 22px;
    position: relative;
    overflow: hidden;
  }

  /* Front side */
  .card-front {
    background: var(--card-white);
    display: flex;
    align-items: center;
  }
  .front-brand {
    width: 265px;
    display: flex;
    justify-content: center;
    align-items: center;
  }
  .brand-name {
    font-weight: 700;
    letter-spacing: 5px;
    text-transform: uppercase;
  }
  .card-front .brand-name { color: var(--navy); font-size: 34px; }
  .divider {
    width: 1px;
    height: 150px;
    background: var(--rule);
  }
  .contact {
    padding-left: 24px;
    color: var(--ink);
    font-size: 12.5px;
    line-height: 1.45;
  }
  .contact-name {
    color: var(--plum);
    font-weight: 700;
    font-size: 19px;
    text-transform: uppercase;
    line-height: 1.1;
  }
  .contact-role { margin-bottom: 10px; font-size: 13px; }
  .contact-line { display: flex; align-items: center; gap: 7px; }
  .contact-line svg { width: 11px; height: 11px; flex: none; }
  .address { margin-top: 10px; }

  /* Back side */
  .card-back {
    background: linear-gradient(150deg, var(--navy) 0%, #3a2478 40%, var(--plum) 72%, var(--magenta) 100%);
    color: var(--white);
  }
  .social {
    position: absolute;
    left: 48px;
    top: 150px;
    display: flex;
    gap: 10px;
  }
  .social-icon {
    width: 30px;
    height: 30px;
    border-radius: 6px;
    background: var(--white);
  }
  .back-brand {
    position: absolute;
    right: 60px;
    top: 120px;
  }
  .card-back .brand-name { font-size: 36px; color: var(--white); }
  .web-links {
    position: absolute;
    right: 48px;
    bottom: 48px;
    text-align: right;
    font-size: 13px;
    line-height: 1.4;
  }
</style>
</head>
<body>
  <section class="card card-front" aria-label="Card front">
    <div class="front-brand">
      <span class="brand-name">Lydgate</span>
    </div>
    <div class="divider"></div>
    <div class="contact">
      <p class="contact-name">Maud Penrose</p>
      <p class="contact-role">Business Development Manager</p>
      <p class="contact-line">
        <svg viewBox="0 0 12 12" aria-hidden="true"><path d="M3 1 L5 3.5 L4 5 Q5 7 7 8 L8.5 7 L11 9 L9.5 11 Q4 10.5 1 2.5 Z" fill="#7a1f86"/></svg>
        +44 (0)1294 730182
      </p>
      <p class="contact-line">
        <svg viewBox="0 0 12 12" aria-hidden="true"><rect x="0.5" y="2.5" width="11" height="7" fill="#7a1f86"/><path d="M0.5 2.5 L6 6.5 L11.5 2.5" stroke="#fff" fill="none"/></svg>
        maudpenrose@lydgatevoyages.example
      </p>
      <p class="contact-line">
        <svg viewBox="0 0 12 12" aria-hidden="true"><circle cx="6" cy="6" r="5.2" fill="none" stroke="#7a1f86" stroke-width="1.2"/><path d="M1 6 H11 M6 1 V11" stroke="#7a1f86" stroke-width="1"/></svg>
        www.lydgatevoyages.example
      </p>
      <p class="address">87 Quarry Lane, Kilwinning,<br>Ayrshire, Scotland KA19 4TN</p>
    </div>
  </section>

  <section class="card card-back" aria-label="Card back">
    <div class="social" aria-label="Social media links">
      <span class="social-icon" role="img" aria-label="Social network icon"></span>
      <span class="social-icon" role="img" aria-label="Social network icon"></span>
      <span class="social-icon" role="img" aria-label="Social network icon"></span>
    </div>
    <div class="back-brand"><span class="brand-name">Lydgate</span></div>
    <div class="web-links">
      <p>www.lydgatevoyages.example</p>
      <p>www.lydgateoutings.example</p>
    </div>
  </section>
</body>
</html>
```